Prepared ready to cook meal delivery service needs a flyer design

We need a flyer design for a startup company based in Cape Town, South Africa. I've attached a few flyer designs that I like.

The company is called 'Pemblo' and our website will be found at pemblo.co.za. We don't have a logo yet.

Flyer text:

Pemblo
Simply sizzle

Do you feel like a home cooked meal but don't like shopping, peeling, chopping, cooking, or cleaning up?

We deliver ready to roast free range chicken and fresh vegetables to your door.

To order: SMS your name to 074 318 6149 and we'll call you back.

Only the best ingredients used
Free range chickens. Fresh herbs and vegetables. Virgin olive oil.

No bad carbs!

Ready to roast Free range chicken and fresh veggies
For 2 R99
For 4 R139
Updates

Wording of flyer updated.

Target Market(s)

Local Cape Townians that hate grocery shopping and need help saving time preparing meals.

Industry/Entity Type

Delivery Service

Requirements
Must have
• To find out more: SMS your name to 074 318 6149

```html
<!DOCTYPE html>
<html lang="en">
<head>
<meta charset="utf-8">
<title>Pemblo – Simply sizzle</title>
<link href="https://fonts.googleapis.com/css2?family=Roboto+Condensed:ital,wght@0,400;0,700;0,900;1,700;1,900&display=swap" rel="stylesheet">
<style>
  :root {
    --red: #d91c1f;
    --red-deep: #b5151a;
    --green: #7cb829;
    --green-dark: #5f9a1c;
    --orange: #f7941d;
    --paper: #f4f8e6;
    --paper-edge: #e3efc4;
    --white: #ffffff;
    --ink-green: #6aa61f;
  }
  * { box-sizing: border-box; margin: 0; padding: 0; }
  html, body { width: 953px; height: 1200px; overflow: hidden; background: #ffffff; }
  body { font-family: "Roboto Condensed", "Arial Narrow", sans-serif; }

  .flyer {
    position: relative;
    width: 953px;
    height: 1200px;
    background: radial-gradient(ellipse at 70% 35%, #ffffff 0%, var(--paper) 45%, var(--paper-edge) 100%);
    overflow: hidden;
  }

  .offer-line {
    position: absolute; top: 52px; left: 0; width: 100%;
    text-align: center; font-size: 38px; font-weight: 400; color: var(--green-dark);
    letter-spacing: -0.3px;
  }
  .offer-line .accent { color: var(--red); }

  .headline-band {
    position: absolute; top: 112px; left: 0; width: 100%; height: 100px;
    background: var(--red);
    display: flex; align-items: center; justify-content: center;
    color: var(--white); font-style: italic; font-weight: 700; font-size: 46px;
    text-transform: uppercase;
  }
  .headline-band .big { font-size: 60px; font-weight: 900; margin-left: 14px; }

  .question-band {
    position: absolute; top: 212px; left: 0; width: 100%; height: 112px;
    background: var(--green);
    display: flex; align-items: center; justify-content: center; text-align: center;
    color: var(--white); font-style: italic; font-weight: 700; font-size: 34px; line-height: 1.2;
  }

  .brand {
    position: absolute; top: 350px; left: 120px;
    display: flex; align-items: center; gap: 26px;
  }
  .brand-dot { width: 110px; height: 110px; border-radius: 50%; background: var(--red); }
  .brand-text { display: flex; flex-direction: column; }
  .brand-tagline {
    font-size: 40px; font-weight: 700; font-style: italic; color: var(--ink-green);
    text-transform: uppercase; letter-spacing: 1px; margin-left: 8px;
  }
  .brand-name {
    font-size: 120px; font-weight: 900; line-height: 0.9; color: var(--green);
    text-transform: uppercase; letter-spacing: 2px;
  }

  .pitch {
    position: absolute; top: 510px; left: 110px; width: 430px;
    text-align: center; font-size: 29px; font-weight: 700; line-height: 1.25; color: var(--ink-green);
  }
  .pitch .accent { color: var(--red); }

  .prices {
    position: absolute; top: 632px; left: 130px; width: 400px; height: 62px;
    background: rgba(255,255,255,0.7);
    display: flex; align-items: center; justify-content: center; gap: 26px;
    font-size: 32px; font-weight: 700; color: var(--ink-green);
  }
  .prices .amount { color: var(--red); font-size: 36px; }

  .meal-photo {
    position: absolute; top: 690px; left: 0; width: 100%; height: 400px;
    background:
      radial-gradient(ellipse 38% 45% at 50% 52%, #b0641e 0%, #d99a45 45%, rgba(240,200,120,0.7) 70%, rgba(255,255,255,0) 100%),
      radial-gradient(ellipse 20% 35% at 8% 40%, #6fae3a 0%, rgba(111,174,58,0) 100%),
      linear-gradient(180deg, rgba(255,255,255,0) 0%, #f2f0e6 60%, #ffffff 100%);
  }

  .order-badge { position: absolute; top: 470px; left: 540px; width: 380px; height: 380px; }

  .quality {
    position: absolute; top: 1092px; left: 0; width: 100%; text-align: center;
  }
  .quality-title {
    font-size: 44px; font-weight: 900; font-style: italic; color: var(--red);
  }
  .quality-detail {
    font-size: 21px; font-weight: 700; font-style: italic; color: var(--green-dark); margin-top: 2px;
  }
</style>
</head>
<body>
  <main class="flyer">
    <p class="offer-line"><span class="accent">Ready to roast</span> Free range chicken and fresh veggies</p>

    <div class="headline-band">Feel like a <span class="big">Home cooked meal?</span></div>
    <div class="question-band">Don't like shopping, peeling, chopping,<br>cooking, or cleaning up?</div>

    <div class="brand">
      <span class="brand-dot" aria-hidden="true"></span>
      <div class="brand-text">
        <span class="brand-tagline">Simply sizzle</span>
        <span class="brand-name">Pemblo</span>
      </div>
    </div>

    <div class="meal-photo" role="img" aria-label="Golden roast free range chicken on a white plate with roast potato wedges, fresh parsley and salad greens"></div>

    <p class="pitch">We deliver <span class="accent">ready to roast</span> free range chicken and fresh vegetables to <span class="accent">your</span> door.</p>

    <div class="prices">
      <span>For 2 <span class="amount">R99</span></span>
      <span>For 4 <span class="amount">R139</span></span>
    </div>

    <svg class="order-badge" viewBox="0 0 380 380" aria-label="SMS your name to 074 318 6149, we'll call you back">
      <defs>
        <path id="callback-arc" d="M 40 190 A 150 150 0 0 1 340 190 A 150 150 0 0 1 290 305"/>
      </defs>
      <circle cx="185" cy="200" r="140" fill="var(--red)"/>
      <text font-family="Roboto Condensed, sans-serif" font-weight="700" font-size="26" fill="#222" letter-spacing="2">
        <textPath href="#callback-arc" startOffset="34%">WE'LL CALL YOU BACK</textPath>
      </text>
      <text x="185" y="195" text-anchor="middle" font-family="Roboto Condensed, sans-serif" font-weight="900" font-size="92" fill="var(--orange)">SMS</text>
      <text x="185" y="240" text-anchor="middle" font-family="Roboto Condensed, sans-serif" font-weight="700" font-size="38" fill="#ffffff">YOUR NAME</text>
      <line x1="80" y1="262" x2="290" y2="262" stroke="var(--orange)" stroke-width="3"/>
      <text x="185" y="302" text-anchor="middle" font-family="Roboto Condensed, sans-serif" font-weight="400" font-size="32" fill="#ffffff">074 318 6149</text>
    </svg>

    <div class="quality">
      <p class="quality-title">Only the best ingredients used</p>
      <p class="quality-detail">Free range chickens. Fresh herbs and vegetables. Virgin olive oil.</p>
    </div>
  </main>
</body>
</html>
```